New and exciting team challenge starting in corporate health. Need a eye catching flyer

Bright Office Quest- http://www.brightofficequest.com. Is a new corporate team wellness program that uses a innovative online platform to track and record users active lifestyle choices. We require a flyer for initial promotion and create a buzz.

Participants goal is to log as many active points as you can on the BOQ APP by completing individual and team challenges and making healthy, active lifestyle choices. The more points you log the closer your team will get to unlocking all 15 Active Levels throughout the 10 week challenge. Each level unlocks information on ancient warrior tribes like the Amazonians. There are plenty of extra trophies to be won along the way, like the ‘Silver Fern’ award for active travel and healthy eating.

Tag line- Your next challenge is here
Final design should leave them wanting more to check out the website. The target will be for those currently exercising. so needs to rope them in with the challenges
Join the Bright Office Quest
- Get rewarded for healthy lifestyle choices daily on the BOQ App
- Compete against teams across Australia and see where you rank
- Complete fun weekly challenges like Hill Crusher and Max Voltage
- Ask Exercise Physiologists and Dietitians all your big questions
- Access 1000’s of exercise programs & videos or create your own and share
- Be a HEALTHIER & HAPPIER YOU

www.brightofficequest.com.au

for more of an idea check out: https://www.videohub-example.com/watch?v=Kp7TzQm4RxA

Hi Everybody, Thanks for your work so far. I have made a small change to the design brief so please have a look. key features has now changed to below- Join the Bright Office Quest to - Get rewarded for healthy lifestyle choices daily on the BOQ App - Compete against teams across the challenge and see where you rank - Complete fun weekly challenges like Hill Crusher and Max Voltage - Ask Exercise Physiologists and Dieticians all your big questions - Access 1000’s of exercise programs & videos or create your own and share

Target Market(s)

Active individuals 30-55yrs old that want to be challenged physically in a fun team environment.
Targeting corporate organisations.

Industry/Entity Type

Travel

Requirements
Must have
• simple and clear to read
Register your interest at www.brightofficequest.com.au
logo
'Your next challenge is here'
' Starts 16th of March'
Find us on Facebook and twitter (use symbols)

Nice to have
• 'The wellness program that challenges, educates and transforms organisations health behaviors'
'What's your lifestyle score?
Should not have
• too many words.

```html
<!DOCTYPE html>
<html lang="en">
<head>
<meta charset="utf-8">
<title>Bright Office Quest – Flyer</title>
<link rel="stylesheet" href="https://fonts.googleapis.com/css2?family=PT+Sans+Narrow:wght@400;700&family=Montserrat:wght@400;500&display=swap">
<style>
  :root {
    --page-bg: #e9e9e9;
    --paper: #ffffff;
    --stripe: rgba(160, 160, 140, 0.28);
    --green-dark: #2f7d1e;
    --green-mid: #4ca82a;
    --lime: #a9cf2c;
    --lime-soft: rgba(169, 207, 44, 0.75);
    --orange: #f26a1b;
    --orange-light: #ff9b2e;
    --text-dark: #222222;
  }
  * { box-sizing: border-box; margin: 0; padding: 0; }
  html, body { width: 1200px; height: 848px; overflow: hidden; }
  body { background: var(--page-bg); position: relative; }

  .flyer {
    position: absolute; left: 320px; top: 26px;
    width: 560px; height: 796px;
    background:
      repeating-linear-gradient(to bottom, transparent 0 8px, var(--stripe) 8px 11px),
      var(--paper);
    overflow: hidden;
    box-shadow: 0 2px 6px rgba(0,0,0,.25);
    font-family: "PT Sans Narrow", "Arial Narrow", sans-serif;
  }
  .flyer__bands { position: absolute; inset: 0; }
  .flyer__content { position: absolute; inset: 0; }

  .headline { position: absolute; left: 0; right: 0; text-align: center; color: var(--green-dark); font-weight: 700; text-transform: uppercase; line-height: 1; }
  .headline--tagline { top: 46px; font-size: 27px; letter-spacing: .3px; }
  .headline--starts { top: 76px; font-size: 21px; color: var(--green-mid); }
  .headline--date { top: 100px; font-size: 46px; }

  .brand { position: absolute; top: 178px; left: 0; right: 0; text-align: center; color: var(--orange); font-family: "Montserrat", sans-serif; font-weight: 500; text-transform: uppercase; line-height: 1.05; }
  .brand__line { display: block; font-size: 42px; letter-spacing: 6px; }
  .brand__line--small { font-size: 34px; letter-spacing: 9px; }

  .feature-tiles { position: absolute; top: 338px; left: 131px; display: flex; gap: 15px; }
  .feature-tile { width: 86px; height: 86px; border-radius: 14px; background: linear-gradient(to bottom, #8fd04a 0%, #4ba82b 48%, #2f8a1c 52%, #3d9c24 100%); box-shadow: 0 2px 4px rgba(0,0,0,.3); }

  .join-heading { position: absolute; color: var(--orange); font-weight: 700; font-size: 25px; text-transform: uppercase; line-height: 1; }
  .join-heading--first { top: 455px; left: 38px; }
  .join-heading--second { top: 485px; left: 156px; }

  .benefits { list-style: none; }
  .benefit { position: absolute; height: 28px; right: 33px; background: linear-gradient(to bottom, var(--orange-light), var(--orange)); color: var(--text-dark); font-family: "PT Sans Narrow", sans-serif; font-size: 14.5px; font-weight: 700; line-height: 28px; padding-left: 18px; white-space: nowrap; }
  .benefit__marker { position: absolute; left: -14px; top: -16px; width: 22px; height: 22px; border-radius: 50%; background: radial-gradient(circle at 40% 35%, #8ed24e, var(--green-mid) 60%, #2c7a18); border: 3px solid #cfe7b4; }
  .benefit__marker::after { content: ""; position: absolute; left: 12px; top: 14px; width: 14px; height: 3px; background: var(--green-mid); transform: rotate(40deg); transform-origin: left center; }

  .square { position: absolute; background: var(--lime); opacity: .85; }
</style>
</head>
<body>
  <article class="flyer">
    <svg class="flyer__bands" width="560" height="796" viewBox="0 0 560 796" aria-hidden="true">
      <g fill="none" stroke="var(--lime-soft)" stroke-width="30" stroke-linejoin="miter">
        <polyline points="-20,0 330,205 600,30"/>
        <polyline points="-20,60 300,250 600,90"/>
        <polyline points="-20,120 280,300 600,160"/>
      </g>
      <g fill="none" stroke="rgba(200,200,190,.35)" stroke-width="1">
        <path d="M300 790 C 360 700, 460 720, 560 690"/>
        <path d="M320 796 C 380 710, 470 735, 560 705"/>
        <path d="M340 796 C 400 725, 480 748, 560 720"/>
      </g>
    </svg>

    <div class="square" style="left:440px;top:355px;width:22px;height:22px"></div>
    <div class="square" style="left:505px;top:395px;width:48px;height:48px"></div>
    <div class="square" style="left:550px;top:370px;width:12px;height:28px"></div>
    <div class="square" style="left:378px;top:442px;width:38px;height:38px"></div>
    <div class="square" style="left:230px;top:440px;width:40px;height:40px"></div>
    <div class="square" style="left:113px;top:478px;width:44px;height:44px"></div>
    <div class="square" style="left:102px;top:432px;width:16px;height:16px"></div>
    <div class="square" style="left:50px;top:477px;width:16px;height:16px"></div>
    <div class="square" style="left:10px;top:452px;width:12px;height:12px"></div>
    <div class="square" style="left:195px;top:478px;width:10px;height:10px"></div>

    <div class="flyer__content">
      <p class="headline headline--tagline">Your next challenge is here</p>
      <p class="headline headline--starts">Starts</p>
      <p class="headline headline--date">16th of March</p>

      <h1 class="brand">
        <span class="brand__line">Bright</span>
        <span class="brand__line brand__line--small">Office Quest</span>
      </h1>

      <div class="feature-tiles">
        <div class="feature-tile" role="img" aria-label="Running person icon"></div>
        <div class="feature-tile" role="img" aria-label="Apple icon"></div>
        <div class="feature-tile" role="img" aria-label="Barbell icon"></div>
      </div>

      <p class="join-heading join-heading--first">Join the Bright</p>
      <p class="join-heading join-heading--second">Office Quest to -</p>

      <ul class="benefits">
        <li class="benefit" style="left:108px;top:539px"><span class="benefit__marker"></span>Get rewarded for healthy lifestyle choices daily on the BOQ App -</li>
        <li class="benefit" style="left:76px;top:586px"><span class="benefit__marker"></span>Compete against teams across the challenge and see where you rank -</li>
        <li class="benefit" style="left:95px;top:632px"><span class="benefit__marker"></span>Complete fun weekly challenges like Hill Crusher and Max Voltage</li>
        <li class="benefit" style="left:121px;top:680px"><span class="benefit__marker"></span>Ask Exercise Physiologists and Dieticians all your big questions</li>
        <li class="benefit" style="left:57px;top:729px"><span class="benefit__marker"></span>Access 1000's of exercise programs &amp; videos or create your own and share</li>
      </ul>
    </div>
  </article>
</body>
</html>
```